Vellmar Detailing – Premium Automotive Detailing Studio Website Design

We're launching a premium automotive detailing studio called Vellmar Detailing, and we’re looking for a clean, minimal, and high-end website design (desktop + mobile version). The studio targets owners of luxury vehicles who care deeply about aesthetics, perfection, and exceptional service.
This project is about more than just showing services , it should feel like a luxury experience from the very first second. The design should be modern, minimalistic, elegant, and clearly aimed at an upscale market.
We’re looking for a designer who can translate our physical studio’s premium interior and architectural feel into a digital presence.
What we want the website to feel like:
Clean and modern
Professional and luxurious
Minimal and not cluttered
Light animations or transitions to add polish
Stylish and cinematic
Design freedom:
We trust your design direction. We are not providing strict color codes or layout instructions, we want you to create what you believe works best based on our brand positioning and target audience. Just keep it premium, modern, and well-organized.
What the website should include:
Hero section with a bold visual (image or video)
About the Studio — a few blocks explaining our story and focus on quality
Service Overview — clearly showing what we offer (detailing, ceramic coating, interior, etc.)
Gallery/Showcase — show off our work with cars, interior, and the space itself
Client Lounge Area — mention comfort, coffee, and waiting space
Testimonials — social proof from satisfied clients
Location & contact section — map, address, contact form
Footer, simple with nav, contact info, and optional social media
Target audience:
Owners of high-end vehicles (Torvani, Kellard, etc.)
Car collectors and detailing enthusiasts
People looking for premium-level service and presentation
Brands/creators booking our photo studio

```html
<!DOCTYPE html>
<html lang="en">
<head>
<meta charset="utf-8">
<title>Vellmar Detailing</title>
<link href="https://fonts.googleapis.com/css2?family=Michroma&family=Inter:wght@400;500;600;700&display=swap" rel="stylesheet">
<style>
:root{
  --bg:#000;
  --panel:#0d0f14;
  --blue:#1a6dff;
  --blue-2:#0a4bff;
  --cyan:#13b4f0;
  --text:#fff;
  --muted:#c9cdd6;
  --field:#fff;
}
*{box-sizing:border-box;margin:0;padding:0}
html,body{width:1200px;height:5352px;overflow:hidden;background:var(--bg);color:var(--text);font-family:"Inter",sans-serif}
.page{position:relative;width:1200px;height:5352px}
.abs{position:absolute}
.display{font-family:"Michroma",sans-serif;font-weight:400;letter-spacing:.5px}
.btn{position:absolute;display:flex;align-items:center;justify-content:center;background:linear-gradient(90deg,var(--cyan),var(--blue));color:#fff;font-size:10px;font-weight:700;text-transform:uppercase;letter-spacing:.4px;border-radius:4px;white-space:nowrap}
.brand{font-family:"Inter",sans-serif;font-weight:700;font-size:22px;letter-spacing:3px;color:#fff;line-height:1}
.social{display:flex;gap:8px}
.social span{width:22px;height:22px;border-radius:50%;background:#fff;display:block}
/* top bar */
.topbar{left:0;top:0;width:1200px;height:33px;background:linear-gradient(90deg,var(--cyan) 0%,var(--blue) 42%,#000 52%,#000 54%,var(--blue) 62%,var(--cyan) 100%)}
.topbar .contact{position:absolute;top:0;height:33px;display:flex;align-items:center;gap:10px;font-size:12px;font-weight:600;white-space:nowrap}
.topbar .ico{width:22px;height:22px;border-radius:50%;background:#fff;display:flex;align-items:center;justify-content:center}
.nav{position:absolute;top:68px;left:420px;display:flex;gap:27px;font-size:10px;font-weight:700;text-transform:uppercase;align-items:center;height:32px;white-space:nowrap}
.nav .active{color:var(--blue);border:1px solid var(--blue);border-radius:50%;padding:8px 6px}
/* hero */
.hero-photo{left:0;top:33px;width:1200px;height:780px;background:radial-gradient(ellipse 55% 40% at 55% 50%,#4a4d54 0%,#2a2b30 35%,#101114 65%,#000 90%)}
.hero h1{position:absolute;left:0;top:152px;width:1200px;text-align:center;font-size:45px;line-height:49px}
.dots{left:560px;top:768px;display:flex;gap:10px;align-items:center}
.dots span{width:6px;height:6px;border-radius:50%;background:#fff}
.dots .on{width:10px;height:10px}
/* headings */
.sec-title{position:absolute;left:0;width:1200px;text-align:center;font-size:36px}
.divider{position:absolute;left:510px;width:180px;height:30px;display:flex;align-items:center;justify-content:center;gap:12px}
.divider i{display:block;width:58px;height:2px;background:var(--blue)}
.divider b{display:block;width:24px;height:24px;border-radius:50%;border:2px solid var(--blue)}
/* welcome */
.emblem{left:131px;top:938px;width:486px;height:360px;display:flex;align-items:center;justify-content:center;background:radial-gradient(ellipse at center,#0b2a7a 0%,#000 70%)}
.emblem span{font-family:"Michroma",sans-serif;font-size:40px;color:var(--blue)}
.welcome h2{position:absolute;left:687px;top:930px;font-size:38px;line-height:44px}
.welcome p{position:absolute;left:687px;top:1032px;width:380px;font-size:13px;line-height:21px;color:var(--muted)}
/* cards */
.card{position:absolute;top:1536px;width:299px;height:436px;background:var(--panel);border-radius:4px}
.card h3{position:absolute;top:20px;width:100%;text-align:center;font-family:"Michroma",sans-serif;font-weight:400;font-size:15px}
.card .img{position:absolute;left:23px;top:54px;width:253px;height:237px}
.card p{position:absolute;left:30px;top:318px;width:239px;text-align:center;font-size:10.5px;line-height:15px;color:var(--muted)}
.card .btn{left:100px;top:378px;width:100px;height:25px;font-size:8px}
.arrow{position:absolute;width:32px;height:32px;border-radius:50%;border:1.5px solid #fff;display:flex;align-items:center;justify-content:center}
/* lounge */
.lounge-bg{left:0;top:2107px;width:1200px;height:675px;background:radial-gradient(ellipse at 40% 40%,#1c1f26 0%,#0a0b0e 60%,#000 100%)}
.lounge h2{position:absolute;left:131px;top:2306px;font-size:38px;line-height:44px}
.lounge p{position:absolute;left:131px;top:2408px;width:345px;font-size:13.5px;line-height:21px;color:var(--muted)}
.lounge-frame{left:880px;top:2340px;width:202px;height:299px;background:var(--blue);border-radius:6px}
.lounge-img{left:563px;top:2309px;width:506px;height:317px;background:linear-gradient(135deg,#3d4a2f 0%,#6f6a5e 45%,#2b2b2e 100%)}
/* gallery */
.tile{position:absolute}
/* testimonials */
.tcard{position:absolute;top:3944px;width:294px;height:302px;background:var(--panel);border-radius:4px;padding:32px 32px}
.tcard .head{display:flex;align-items:center;gap:10px}
.tcard .q{width:32px;height:32px;border-radius:50%;background:var(--blue);display:flex;align-items:center;justify-content:center;font-size:22px;font-weight:700}
.tcard .name{font-size:13px;font-weight:600}
.tcard .stars{color:#ff9a1f;font-size:11px;letter-spacing:1px}
.tcard p{margin-top:14px;font-size:10.5px;line-height:15.5px;color:var(--muted)}
/* map + forms */
.map{left:0;top:4297px;width:1200px;height:575px;background:linear-gradient(160deg,#dfe8d6 0%,#eef0e6 40%,#cfe3c7 75%,#e7eadf 100%)}
.quote{left:131px;top:4677px;width:479px;height:382px;background:var(--blue-2)}
.contactbox{left:610px;top:4677px;width:459px;height:382px;background:linear-gradient(135deg,var(--cyan),#1aa8ee)}
.panel-title{position:absolute;top:44px;font-size:30px;white-space:nowrap}
.field{position:absolute;background:var(--field);border-radius:2px;color:#7a7f88;font-size:9px;padding:11px 14px}
.citem{position:absolute;left:44px;display:flex;gap:16px;font-size:12.5px;line-height:18px}
.citem .ci{width:30px;height:30px;border-radius:50%;background:#fff;display:flex;align-items:center;justify-content:center;flex:none}
/* footer */
.footnav{position:absolute;top:5146px;left:403px;display:flex;gap:40px;font-size:12px;font-weight:600}
.copy{position:absolute;left:0;top:5276px;width:1200px;text-align:center;font-size:13px}
</style>
</head>
<body>
<div class="page">

  <!-- Top bar -->
  <div class="abs topbar">
    <div class="social" style="position:absolute;left:131px;top:5px">
      <span></span><span></span><span></span><span></span><span></span>
    </div>
    <div class="contact" style="left:616px">
      <div class="ico"><svg width="12" height="12" viewBox="0 0 24 24"><path fill="#1a6dff" d="M6.6 10.8a15.1 15.1 0 0 0 6.6 6.6l2.2-2.2c.3-.3.7-.4 1-.2 1.1.4 2.3.6 3.6.6.6 0 1 .4 1 1V20c0 .6-.4 1-1 1A17 17 0 0 1 3 4c0-.6.4-1 1-1h3.5c.6 0 1 .4 1 1 0 1.3.2 2.5.6 3.6.1.3 0 .7-.2 1z"/></svg></div>
      Call +1 555 0142 7788
    </div>
    <div class="contact" style="left:824px">
      <div class="ico"><svg width="12" height="12" viewBox="0 0 24 24"><path fill="#1a6dff" d="M3 5h18v14H3zm2 2v.5l7 4.5 7-4.5V7z"/></svg></div>
      info@vellmardetailing.com
    </div>
    <svg class="abs" style="left:1052px;top:7px" width="19" height="19" viewBox="0 0 24 24"><circle cx="10" cy="10" r="7" fill="none" stroke="#fff" stroke-width="2"/><path d="M15 15l6 6" stroke="#fff" stroke-width="2"/></svg>
  </div>

  <!-- Hero -->
  <section class="hero">
    <div class="abs hero-photo" role="img" aria-label="Detailer washing a foam-covered sports car in a dark studio"></div>
    <div class="abs brand" style="left:131px;top:72px">VELLMAR<br><span style="font-size:11px;letter-spacing:6px;font-weight:700">DETAILING</span></div>
    <nav class="nav">
      <span class="active">Home</span><span>About</span><span>Services</span><span>Gallery</span><span>Location</span><span>Contact</span>
    </nav>
    <div class="btn" style="left:901px;top:68px;width:168px;height:32px;font-size:9px">Book an appointment</div>
    <h1 class="display">Vellmar Detailing<br>Where Precision Meets<br>Perfection</h1>
    <div class="btn" style="left:509px;top:322px;width:182px;height:37px;font-size:9px">Explore our services</div>
    <svg class="abs" style="left:0;top:640px" width="1200" height="180" viewBox="0 0 1200 180">
      <polygon points="0,30 486,160 486,180 0,48" fill="#1a6dff"/>
      <polygon points="1200,30 768,160 768,180 1200,48" fill="#1a6dff"/>
      <polygon points="0,48 486,180 0,180" fill="#000"/>
      <polygon points="1200,48 768,180 1200,180" fill="#000"/>
      <rect x="486" y="160" width="282" height="20" fill="#000"/>
    </svg>
    <div class="abs dots"><span></span><span></span><span class="on"></span><span></span><span></span></div>
  </section>

  <!-- Welcome -->
  <section class="welcome">
    <div class="abs emblem" role="img" aria-label="Vellmar Detailing emblem"><span>VELLMAR</span></div>
    <h2 class="display">Welcome to<br>Vellmar Detailing</h2>
    <p>At Vellmar Detailing, we serve car enthusiasts who expect nothing short of perfection. Our studio is a sanctuary of craftsmanship where luxury vehicles receive meticulous care using the highest quality products, tools, and techniques. Whether it's a collector's Marenzo or a daily-driven Kellard, we approach every detail with reverence and precision.</p>
    <div class="btn" style="left:687px;top:1206px;width:125px;height:37px;font-size:9px">Learn more</div>
  </section>

  <!-- Services -->
  <section class="services">
    <h2 class="sec-title display" style="top:1396px">Our Services</h2>
    <div class="divider" style="top:1459px"><i></i><b></b><i></i></div>
    <div class="arrow" style="left:75px;top:1738px"><svg width="14" height="10" viewBox="0 0 14 10"><path d="M13 5H1M5 1L1 5l4 4" stroke="#fff" fill="none" stroke-width="1.5"/></svg></div>
    <div class="arrow" style="left:1091px;top:1738px"><svg width="14" height="10" viewBox="0 0 14 10"><path d="M1 5h12M9 1l4 4-4 4" stroke="#fff" fill="none" stroke-width="1.5"/></svg></div>
    <article class="card" style="left:131px">
      <h3>Exterior Detailing</h3>
      <div class="img" role="img" aria-label="Red sports car being polished in a studio" style="background:linear-gradient(135deg,#2a2d33,#8c1018 55%,#1a1a1d)"></div>
      <p>Deep cleaning, decontamination, and shine enhancement. Sed ut perspiciatis unde omnis iste natus sit voluptatem accusantium</p>
      <div class="btn">Learn more</div>
    </article>
    <article class="card" style="left:450px">
      <h3>Ceramic Coating</h3>
      <div class="img" role="img" aria-label="Blue car panel being machine polished" style="background:linear-gradient(135deg,#0a1a4a,#1a3fb0 50%,#0b0d18)"></div>
      <p>Long-lasting hydrophobic protection with unmatched gloss. Sed ut perspiciatis unde omnis iste natus sit voluptatem</p>
      <div class="btn">Learn more</div>
    </article>
    <article class="card" style="left:768px">
      <h3>Interior Detailing</h3>
      <div class="img" role="img" aria-label="Hand wiping a car interior console with a cloth" style="background:linear-gradient(135deg,#c9b8a8,#6d8fc0 45%,#1b1c20)"></div>
      <p>Upholstery care, deep vacuuming, leather conditioning. Sed ut perspiciatis unde omnis iste natus sit voluptatem accusantium</p>
      <div class="btn">Learn more</div>
    </article>
  </section>

  <!-- Client lounge -->
  <section class="lounge">
    <div class="abs lounge-bg" role="img" aria-label="Dark moonlit backdrop with a car silhouette"></div>
    <svg class="abs" style="left:0;top:2107px" width="1200" height="160" viewBox="0 0 1200 160">
      <polygon points="0,155 486,10 486,22 0,160" fill="#1a6dff"/>
      <polygon points="1200,155 768,10 768,22 1200,160" fill="#1a6dff"/>
    </svg>
    <h2 class="display">Client<br>Lounge Area</h2>
    <p>Sed ut perspiciatis unde omnis iste natus error sit voluptatem accusantium doloremque laudantium, totam rem aperiam, eaque ipsa quae ab illo inventore veritatis et quasi architecto beatae vitae dicta sunt explicabo. Nemo enim ipsam voluptatem quia voluptas sit aspernatur aut odit aut fugit, sed quia consequuntur magni dolores</p>
    <div class="btn" style="left:131px;top:2585px;width:125px;height:35px;font-size:9px">Learn more</div>
    <div class="abs lounge-frame"></div>
    <div class="abs lounge-img" role="img" aria-label="Clients chatting in the lounge with a laptop and coffee"></div>
  </section>

  <!-- Gallery -->
  <section class="gallery">
    <h2 class="sec-title display" style="top:2866px">Our Gallery</h2>
    <div class="divider" style="top:2931px"><i></i><b></b><i></i></div>
    <div class="tile" role="img" aria-label="Red sports car being washed" style="left:131px;top:3010px;width:297px;height:297px;background:linear-gradient(135deg,#3a3d44,#8e1016 60%,#111)"></div>
    <div class="tile" role="img" aria-label="Gloved hand polishing a blue panel" style="left:450px;top:3010px;width:297px;height:297px;background:linear-gradient(135deg,#0d0f14,#1f4fd0 55%,#b9bcc2)"></div>
    <div class="tile" role="img" aria-label="Detailer polishing a red car headlight" style="left:770px;top:3010px;width:299px;height:297px;background:linear-gradient(135deg,#d8d9dc,#a80f18 50%,#1b1b1d)"></div>
    <div class="tile" role="img" aria-label="Cleaning a black alloy wheel" style="left:131px;top:3328px;width:457px;height:297px;background:linear-gradient(135deg,#b01620,#1c1d21 50%,#0a0a0b)"></div>
    <div class="tile" role="img" aria-label="Brush cleaning an interior center console" style="left:610px;top:3328px;width:459px;height:297px;background:linear-gradient(135deg,#1a1b1e,#4b4d52 55%,#0f1012)"></div>
    <div class="btn" style="left:507px;top:3677px;width:186px;height:39px;font-size:9px">See all gallery</div>
  </section>

  <!-- Testimonials -->
  <section class="testimonials">
    <h2 class="sec-title display" style="top:3792px">Testimonials</h2>
    <div class="divider" style="top:3855px"><i></i><b></b><i></i></div>
    <div class="arrow" style="left:75px;top:4049px"><svg width="14" height="10" viewBox="0 0 14 10"><path d="M13 5H1M5 1L1 5l4 4" stroke="#fff" fill="none" stroke-width="1.5"/></svg></div>
    <div class="arrow" style="left:1091px;top:4049px"><svg width="14" height="10" viewBox="0 0 14 10"><path d="M1 5h12M9 1l4 4-4 4" stroke="#fff" fill="none" stroke-width="1.5"/></svg></div>
    <article class="tcard" style="left:131px">
      <div class="head"><div class="q">“</div><div><div class="name">John Doe</div><div class="stars">★★★★★</div></div></div>
      <p>"Sed ut perspiciatis unde omnis iste natus error sit voluptatem accantium doloremque laudantium, totam rem aperiam, eaque ipsa quae ab illo inventore veritatis et quasi arcecto beatae vitae dicta sunt explicabo. Nemo enim ipsam voluptatem quia voluptas sit asperatur aut odit aut fugit, sed quia consequuntur magni dolores eos qui"</p>
    </article>
    <article class="tcard" style="left:453px">
      <div class="head"><div class="q">“</div><div><div class="name">John Doe</div><div class="stars">★★★★★</div></div></div>
      <p>"Sed ut perspiciatis unde omnis iste natus error sit voluptatem accantium doloremque laudantium, totam rem aperiam, eaque ipsa quae ab illo inventore veritatis et quasi arcecto beatae vitae dicta sunt explicabo. Nemo enim ipsam voluptatem quia voluptas sit asperatur aut odit aut fugit, sed quia consequuntur magni dolores eos qui"</p>
    </article>
    <article class="tcard" style="left:775px">
      <div class="head"><div class="q">“</div><div><div class="name">John Doe</div><div class="stars">★★★★★</div></div></div>
      <p>"Sed ut perspiciatis unde omnis iste natus error sit voluptatem accantium doloremque laudantium, totam rem aperiam, eaque ipsa quae ab illo inventore veritatis et quasi arcecto beatae vitae dicta sunt explicabo. Nemo enim ipsam voluptatem quia voluptas sit asperatur aut odit aut fugit, sed quia consequuntur magni dolores eos qui"</p>
    </article>
  </section>

  <!-- Location + contact -->
  <section class="location">
    <div class="abs map" role="img" aria-label="Regional map showing studio locations"></div>
    <div class="abs quote">
      <h2 class="panel-title display" style="left:37px">Request a Quote</h2>
      <div class="divider" style="top:88px;left:37px;width:110px;gap:8px"><i style="width:30px;background:#fff"></i><b style="border-color:#fff;width:20px;height:20px"></b><i style="width:30px;background:#fff"></i></div>
      <div class="field" style="left:37px;top:133px;width:197px;height:33px">Your name</div>
      <div class="field" style="left:245px;top:133px;width:197px;height:33px">Phone</div>
      <div class="field" style="left:37px;top:179px;width:197px;height:33px">Email address</div>
      <div class="field" style="left:245px;top:179px;width:197px;height:33px">Vehicle Make/Model</div>
      <div class="field" style="left:37px;top:226px;width:405px;height:63px">Message</div>
      <div class="abs" style="left:37px;top:307px;width:137px;height:34px;background:#000;border-radius:3px;display:flex;align-items:center;justify-content:center;font-size:9px;font-weight:700">SUBMIT</div>
    </div>
    <div class="abs contactbox">
      <h2 class="panel-title display" style="left:44px">Contact Us</h2>
      <div class="divider" style="top:88px;left:44px;width:110px;gap:8px"><i style="width:30px;background:#fff"></i><b style="border-color:#fff;width:20px;height:20px"></b><i style="width:30px;background:#fff"></i></div>
      <div class="citem" style="top:135px"><div class="ci"><svg width="12" height="14" viewBox="0 0 24 28"><path fill="#1a6dff" d="M12 0a10 10 0 0 0-10 10c0 7.5 10 18 10 18s10-10.5 10-18A10 10 0 0 0 12 0zm0 14a4 4 0 1 1 0-8 4 4 0 0 1 0 8z"/></svg></div><div>Location:<br>Morbi iaculis turpis non<br>molestie faucibus</div></div>
      <div class="citem" style="top:206px"><div class="ci"><svg width="12" height="12" viewBox="0 0 24 24"><path fill="#1a6dff" d="M6.6 10.8a15.1 15.1 0 0 0 6.6 6.6l2.2-2.2c.3-.3.7-.4 1-.2 1.1.4 2.3.6 3.6.6.6 0 1 .4 1 1V20c0 .6-.4 1-1 1A17 17 0 0 1 3 4c0-.6.4-1 1-1h3.5c.6 0 1 .4 1 1 0 1.3.2 2.5.6 3.6.1.3 0 .7-.2 1z"/></svg></div><div>Phone:<br>+1 555 0142 7788</div></div>
      <div class="citem" style="top:272px"><div class="ci"><svg width="12" height="12" viewBox="0 0 24 24"><path fill="#1a6dff" d="M3 5h18v14H3zm2 2v.5l7 4.5 7-4.5V7z"/></svg></div><div>Email:<br>info@vellmardetailing.com</div></div>
    </div>
  </section>

  <!-- Footer -->
  <footer>
    <div class="abs brand" style="left:131px;top:5140px">VELLMAR<br><span style="font-size:11px;letter-spacing:6px;font-weight:700">DETAILING</span></div>
    <nav class="footnav"><span>Home</span><span>About</span><span>Services</span><span>Gallery</span><span>Location</span><span>Contact</span></nav>
    <div class="social abs" style="left:922px;top:5146px"><span></span><span></span><span></span><span></span><span></span></div>
    <div class="copy">Vellmar Detailing © 2025. All Rights Reserved.</div>
  </footer>

</div>
</body>
</html>
```